Falcon guarding business card

Looking for a business card for my security company

Target Market(s)

Security

Industry/Entity Type

Security

Contact Information for Business Card

Name - Dale Hutchins. Title - General manager - direct 318 642.9053 website www. falconguardingservices.example email - dale@ falconguardingservices.example

Requirements
Must have
• Logo attached

```html
<!DOCTYPE html>
<html lang="en">
<head>
<meta charset="utf-8">
<title>Falcon Guarding – Business Card</title>
<link rel="stylesheet" href="https://fonts.googleapis.com/css2?family=Arimo:wght@400;700&display=swap">
<style>
  :root {
    --stage: #2b2b2b;
    --card: #1f1f1f;
    --card-back: #1c1c1c;
    --gold: #c8913a;
    --gold-light: #e3b55e;
    --ink: #f2f2f2;
    --emboss: #2e2e2e;
  }
  * { box-sizing: border-box; margin: 0; padding: 0; }
  html, body { width: 1200px; height: 900px; overflow: hidden; }
  body {
    background: var(--stage);
    font-family: "Arimo", Arial, sans-serif;
    display: flex; flex-direction: column; align-items: center; justify-content: center;
    gap: 50px;
  }
  .card {
    position: relative;
    width: 640px; height: 366px;
    background: var(--card);
    border-left: 2px solid var(--gold);
    border-bottom: 2px solid var(--gold);
    box-shadow: 0 12px 30px rgba(0,0,0,.45);
  }
  /* Front */
  .identity { position: absolute; left: 48px; top: 128px; }
  .identity__name {
    color: var(--gold); font-weight: 700; font-size: 24px; letter-spacing: .5px;
    text-transform: uppercase; line-height: 1.1;
  }
  .identity__title { color: var(--ink); font-size: 15px; margin-top: 6px; }
  .rule {
    position: absolute; left: 44px; right: 44px; top: 196px;
    height: 1px; background: var(--gold);
  }
  .contact-list { list-style: none; position: absolute; left: 48px; top: 226px; }
  .contact-list__item {
    color: var(--ink); font-size: 14px; display: flex; align-items: center; gap: 8px; margin-bottom: 10px;
  }
  .icon { width: 14px; height: 14px; flex: none; fill: var(--gold-light); }
  .brand {
    position: absolute; right: 48px; top: 132px;
    display: flex; align-items: center; gap: 10px;
  }
  .brand__dot { width: 16px; height: 16px; border-radius: 50%; background: var(--gold); }
  .brand__name { color: var(--gold); font-weight: 700; font-size: 28px; text-transform: uppercase; line-height: 1; }
  .website {
    position: absolute; right: 48px; bottom: 34px;
    color: var(--ink); font-size: 14px; display: flex; align-items: center; gap: 8px;
  }
  /* Back */
  .card--back { background: var(--card-back); display: flex; align-items: center; justify-content: center; }
  .brand--large { position: static; }
  .brand--large .brand__name { font-size: 52px; color: var(--emboss); }
  .brand--large .brand__dot { width: 30px; height: 30px; background: var(--emboss); }
</style>
</head>
<body>

<section class="card card--front">
  <div class="identity">
    <h1 class="identity__name">Dale Hutchins</h1>
    <p class="identity__title">General manager</p>
  </div>
  <div class="brand">
    <span class="brand__dot"></span>
    <span class="brand__name">Falcon guarding</span>
  </div>
  <div class="rule"></div>
  <ul class="contact-list">
    <li class="contact-list__item">
      <svg class="icon" viewBox="0 0 24 24"><path d="M6.6 10.8a15.1 15.1 0 0 0 6.6 6.6l2.2-2.2c.3-.3.7-.4 1-.2 1.1.4 2.3.6 3.6.6.6 0 1 .4 1 1V20c0 .6-.4 1-1 1A17 17 0 0 1 3 4c0-.6.4-1 1-1h3.5c.6 0 1 .4 1 1 0 1.3.2 2.5.6 3.6.1.3 0 .7-.2 1z"/></svg>
      318 642.9053
    </li>
    <li class="contact-list__item">
      <svg class="icon" viewBox="0 0 24 24"><path d="M2 5h20v14H2z M3.5 6.5 12 13l8.5-6.5" fill="none" stroke="#e3b55e" stroke-width="2"/></svg>
      dale@falconguardingservices.example
    </li>
  </ul>
  <p class="website">
    <svg class="icon" viewBox="0 0 24 24"><circle cx="12" cy="12" r="9" fill="none" stroke="#e3b55e" stroke-width="2"/><path d="M3 12h18M12 3c3 3 3 15 0 18M12 3c-3 3-3 15 0 18" fill="none" stroke="#e3b55e" stroke-width="1.5"/></svg>
    www.falconguardingservices.example
  </p>
</section>

<section class="card card--back">
  <div class="brand brand--large">
    <span class="brand__dot"></span>
    <span class="brand__name">Falcon guarding</span>
  </div>
</section>

</body>
</html>
```